Text only wordpress site to capture emails

Refer to inspiration upload for list of sites that will be useful for you.

We need a site that will be used to capture emails from clients that follow us on social media. The site will be all text, pretty simple. I have a couple of text sites that I like and we can use them for an example.

Menu section will have home, archive, about.
Footer will have © and Website Privacy Policy | Legal and Policies
There will be some text on the home page and an email capture.

This site will be all text no pictures.

I discuss office politics so the text portions will have some questions and answers on this and then prompt for the visitor to subscribe to my email list.

The only purpose of the site is to build an email list from existing social media followers so the site will be pretty simple in and of itself.

• Text only, similar Q&A to uploaded pics.

I will use a template from mail lantern dotcom for email capture.

I like the simple couriernew font family that is on both sites supplied in the uploads.
• If you use any color it needs to be very minimal.

```html
<!DOCTYPE html>
<html lang="en">
<head>
<meta charset="utf-8">
<title>Northbay Ventures</title>
<link rel="stylesheet" href="https://fonts.googleapis.com/css2?family=Courier+Prime:wght@400;700&display=swap">
<style>
  :root {
    --paper: #f7f7f4;
    --ink: #1f1f1f;
    --accent: #2b3592;
    --rule: #d6d6d0;
    --muted: #6b6b6b;
    --white: #ffffff;
  }
  * { box-sizing: border-box; margin: 0; padding: 0; }
  html, body { width: 1200px; height: 617px; overflow: hidden; }
  body { background: var(--paper); font-family: "Courier Prime", "Courier New", monospace; color: var(--ink); }
  .page { position: relative; width: 1200px; height: 617px; background: var(--paper); overflow: hidden; }

  .brand {
    position: absolute; left: 77px; top: 36px;
    font-size: 22px; font-weight: 700; color: var(--accent); letter-spacing: 0.2px;
  }
  .main-nav { position: absolute; top: 41px; left: 434px; display: flex; gap: 41px; }
  .main-nav a {
    color: var(--ink); text-decoration: none; font-size: 14px; font-weight: 700;
    text-transform: uppercase;
  }
  .login-button {
    position: absolute; left: 954px; top: 27px; width: 151px; height: 45px;
    border-radius: 23px; background: var(--accent); color: var(--white);
    display: flex; align-items: center; justify-content: center;
    font-size: 14px; font-weight: 700; text-decoration: none;
  }

  .hero-title {
    position: absolute; left: 78px; top: 150px; width: 600px;
    font-size: 32px; line-height: 46.5px; font-weight: 700; color: var(--ink);
  }
  .hero-title span { display: block; white-space: nowrap; }

  .subscribe-form {
    position: absolute; left: 78px; top: 322px; width: 489px; height: 55px;
    display: flex; border: 1px solid var(--rule); border-radius: 6px; overflow: hidden;
    background: var(--white);
  }
  .subscribe-form input {
    flex: 1; min-width: 0; border: none; background: var(--white); padding: 0 19px;
    font-family: "Courier Prime", "Courier New", monospace; font-size: 13px; color: var(--ink);
    outline: none;
  }
  .subscribe-form input::placeholder { color: var(--muted); }
  .subscribe-form button {
    width: 146px; border: none; background: var(--accent); color: var(--white);
    font-family: "Courier Prime", "Courier New", monospace; font-size: 16px; font-weight: 700;
    border-radius: 5px; cursor: pointer;
  }

  .hero-text {
    position: absolute; left: 79px; top: 403px; width: 490px;
    font-size: 13px; line-height: 30px; color: var(--ink);
  }

  .site-footer {
    position: absolute; left: 78px; top: 586px;
    display: flex; gap: 12px; align-items: center;
    font-size: 11.5px; color: var(--muted);
  }
  .site-footer a { color: var(--muted); text-decoration: none; }
</style>
</head>
<body>
  <div class="page">
    <header>
      <div class="brand">NORTHBAY VENTURES</div>
      <nav class="main-nav">
        <a href="#">Home</a>
        <a href="#">Archive</a>
        <a href="#">About</a>
        <a href="#">Contact Us</a>
      </nav>
      <a class="login-button" href="#">LOGIN</a>
    </header>

    <main>
      <h1 class="hero-title">
        <span>Lorem ipsum dolor sit amet</span>
        <span>consectetur adipiscing elit</span>
        <span>sed do eiusmod tempor</span>
      </h1>

      <form class="subscribe-form" action="#">
        <input type="email" placeholder="Enter your email here" aria-label="Email address">
        <button type="submit">SUBSCRIBE</button>
      </form>

      <p class="hero-text">Lorem ipsum dolor sit amet, consectetur adipiscing elit, sed do eiusmod tempor incididunt ut labore et dolore magna aliqua. Quis ipsum suspendisse ultrices gravida. Risus commodo.</p>
    </main>

    <footer class="site-footer">
      <span>© Copyrights 2021 Company Name</span>
      <span>|</span>
      <a href="#">Privacy Policy</a>
      <span>|</span>
      <a href="#">Legal and Policies</a>
    </footer>
  </div>
</body>
</html>
```